'TOLVANTA' NEW WINE LABEL DESIGN

I am looking for an exceptional and exciting design for a wine label called 'Tolvanta' meaning 'Lookout'. The design must feature the name 'Tolvanta', and the word 'Cabernet Sauvignon' in version 1 and 'Sauvignon Blanc' in version 2. It will also need the words 'Valle Central, Chile' at the bottom of the label as a prominent piece of information as well as the vintage 2017. Please produce the work in size 80mm x 100mm. Feel free to use colour in addition to black/white and ensue that the label is easy to read on a shelf placement.
Target Market(s)
SUPERMARKETS & WINE STORES
Requirements
Must have
- EASY TO READ, USE COLOURS LIKE GREEN FOR SAUVIGNON & RED FOR CABERNET SAUVIGNON
- FULL BOTTLE SHOT MUST BE IN PROVIDED DESIGNS. ALL BOTTLE TOPS SHOULD BE QUORLAN STYLE (SCREW TOP)
- PLEASE NOTE THAT LABEL INFORMATION MUSY BE EASY TO READ I.E. VINTAGE, PLACE OF ORGIN ALTHOUGH NOT THE MAIN CONTENT MUST STILL BE CLEAR.
Nice to have
- ARTISTIC REFERENCE LINK TO NAME & ANDES BUT NOT PICTURES OF MOUNTAINS
Should not have
- PICTURES OF GRAPES
- PICTURES OF VINEYARDS
- PICTURES OF MOUNTAINS

```html
<!DOCTYPE html>
<html lang="en">
<head>
<meta charset="utf-8">
<title>Tolvanta wine labels</title>
<link href="https://fonts.googleapis.com/css2?family=Cinzel:wght@700&family=Alegreya:wght@700&family=Cormorant+Garamond:wght@600;700&display=swap" rel="stylesheet">
<style>
  :root {
    --page: #ffffff;
    --label: #ffffff;
    --ink: #111111;
    --cabernet: #b3171f;
    --cabernet-soft: #e7a3a6;
    --blanc: #7fba3a;
    --blanc-soft: #cde4ad;
    --edge: #e4e4e4;
  }
  * { margin: 0; padding: 0; box-sizing: border-box; }
  html, body {
    width: 781px;
    height: 1200px;
    overflow: hidden;
    background: var(--page);
  }
  .label-set {
    width: 781px;
    height: 1200px;
    display: flex;
    justify-content: center;
    align-items: center;
    gap: 27px;
  }
  .label {
    width: 350px;
    height: 438px;
    background: var(--label);
    border: 1px solid var(--edge);
    position: relative;
    text-align: center;
  }
  .label--cabernet { --accent: var(--cabernet); --accent-soft: var(--cabernet-soft); }
  .label--blanc { --accent: var(--blanc); --accent-soft: var(--blanc-soft); }
  .brand {
    position: absolute;
    top: 30px;
    left: 0;
    right: 0;
    font-family: "Cinzel", serif;
    font-weight: 700;
    font-size: 42px;
    letter-spacing: 1px;
    color: var(--ink);
  }
  .artwork {
    position: absolute;
    top: 92px;
    left: 0;
    right: 0;
    height: 210px;
    background: linear-gradient(180deg, var(--label) 0%, #f2f2f2 22%, var(--accent-soft) 52%, var(--accent) 100%);
  }
  .variety {
    position: absolute;
    top: 318px;
    left: 0;
    right: 0;
    font-family: "Alegreya", serif;
    font-weight: 700;
    font-size: 26px;
    color: var(--accent);
  }
  .vintage {
    position: absolute;
    top: 361px;
    left: 0;
    right: 0;
    display: flex;
    justify-content: center;
    align-items: center;
    gap: 10px;
    font-family: "Cormorant Garamond", serif;
    font-weight: 700;
    font-size: 16px;
    color: var(--ink);
  }
  .vintage__rule {
    width: 30px;
    height: 2px;
    background: var(--ink);
  }
  .origin {
    position: absolute;
    top: 393px;
    left: 0;
    right: 0;
    font-family: "Cormorant Garamond", serif;
    font-weight: 700;
    font-size: 12px;
    letter-spacing: 1.4px;
    text-transform: uppercase;
    color: var(--ink);
  }
</style>
</head>
<body>
  <main class="label-set">
    <section class="label label--cabernet">
      <h1 class="brand">TOLVANTA</h1>
      <div class="artwork" role="img" aria-label="Engraved condor perched on a rocky peak holding a bunch of grapes, above a red-tinted valley landscape"></div>
      <h2 class="variety">Cabernet Sauvignon</h2>
      <p class="vintage"><span class="vintage__rule"></span>2017<span class="vintage__rule"></span></p>
      <p class="origin">Valle Central | Wine of Chile</p>
    </section>
    <section class="label label--blanc">
      <h1 class="brand">TOLVANTA</h1>
      <div class="artwork" role="img" aria-label="Engraved condor perched on a rocky peak holding a bunch of grapes, above a green-tinted valley landscape"></div>
      <h2 class="variety">Sauvignon Blanc</h2>
      <p class="vintage"><span class="vintage__rule"></span>2017<span class="vintage__rule"></span></p>
      <p class="origin">Valle Central | Wine of Chile</p>
    </section>
  </main>
</body>
</html>
```